Artificial Intelligence Software Product Microsite

We specialises in Artificial Intelligence (AI) technology for big data analytics and we have a new product to be launched and requires a product microsite for it. Our product is an AI-driven Predictive/Prescriptive Analytics Engine that does the job of a Data Scientist or a group of Data Scientists, highly intelligent and fully automated, where endusers do not require any machine-learning knowledge. We would like to see a design that's simple yet futuristic and provide an impression that it is highly technological advanced. Key messages to deliver are that it is first of its kind in the world, it deploys state-of-the-art technology, a solution that is easy to adopt and integrate into their existing or planned apps. It is in effect a (or a pool of) Virtual Data Scientist(s) at their disposal that will work for them tirelessly 365 days a year and at a small fraction of the cost of a data scientist. Will provide more details, files/images only to shortlisted designers. Expecting something that is simple and straightforward that sufficiently showcase the product/technology.

Deadline will be extended if necessary to facilitate shortlisted designers.
Updates

Reason: To provide designers with more time for submission and amendments. For those who have not submitted your design, pls do so ASAP and also submit your concept first. Pls ensure that you are designing a Product Micro-site and not a corporate website. It's meant to introduce the product only, not the company. Only an enquiry email address is to be included at the bottom. Already said in my earlier public comments, would want something that is scroll-down to view more info rather then having to click to view different pages. This is a pre-requisite as stated both in my project brief and public comments. Thank you for participating and looking forward to see something really good soon.

Target Market(s)

App Developers in the Software Industry or any Enterprise Customers with in-house apps.

Industry/Entity Type

Computer Software

Coding

Coded - Design and coding required

Number of Pages Required

3 page

Font styles to use
Other font styles liked:
• Pls refer to attachments.

Requirements
Must have
• Please refer to the attached document "VandrelAI 1-page Infosheet". Key message to be delivered is as per this document but need to add in additional information on performance comparisons, which is a small section but only ready on 10th Jul. The microsite doesn't have to be strictly 3 pages but can be less or more if necessary but do go along the lines of the modern sites whereby when options are clicked, the page slides down to the specific option selected instead. Prefers some simple animation, especially for the diagram that depicts the high-level architecture of our AI engine, how the process flows between the different components. Make it simple yet futuristic. The key theme or focal point is "Virtual Data Scientist". Would like to see something that's short and straight to the point, with a clean design.
Nice to have
• If you can use suitable images of a (or group of) human data scientist(s) depicting the transformation to a "Virtual Data Scientist" will be great.
Should not have
• This is a software technology to be introduced and as such, must have a design or theme appropriate for the industry. It should not have the kind of generic look-and-feel that other industries uses.

```html
<!DOCTYPE html>
<html lang="en">
<head>
<meta charset="utf-8">
<title>VandrelAI – Virtual Data Scientist</title>
<link rel="stylesheet" href="https://fonts.googleapis.com/css2?family=Oswald:wght@400;500&family=Open+Sans:wght@400;600;700&display=swap">
<style>
:root{
  --red:#d8262e;
  --ink:#333;
  --muted:#777;
  --hero:#dfe7ec;
  --line:#e6e6e6;
  --foot:#f1f1f1;
  --bar:#2b2b2b;
  --teal:#2bb3c0;
  --orange:#f39a1e;
  --blue:#2f7fc1;
}
*{margin:0;padding:0;box-sizing:border-box}
html,body{width:720px;height:1200px;overflow:hidden;background:#fff}
body{font-family:"Open Sans",Arial,sans-serif;color:var(--ink);font-size:8px;line-height:1.45}
.page{width:720px;height:1200px;position:relative}

.site-header{height:72px;display:flex;align-items:center;justify-content:space-between;padding:0 40px 0 28px;border-bottom:1px solid var(--line)}
.brand{display:flex;align-items:center;gap:6px;font-family:"Open Sans",sans-serif;font-weight:700;font-size:20px;color:var(--red)}
.brand-mark{width:12px;height:12px;background:var(--red)}
.main-nav{display:flex;gap:4px}
.main-nav a{font-size:8px;font-weight:600;color:var(--ink);text-decoration:none;padding:6px 9px;letter-spacing:.4px}
.main-nav a.active{background:var(--red);color:#fff}

.hero{height:324px;background:var(--hero);position:relative;display:flex;align-items:center;padding:0 40px}
.hero-art{width:290px;height:270px;border-radius:8px;background:radial-gradient(circle at 50% 60%,#5fb2e6 0%,#8fcbef 35%,#cfe3ee 70%,var(--hero) 100%)}
.hero-text{margin-left:30px;margin-top:40px}
.hero-title{font-family:"Oswald",sans-serif;font-weight:500;font-size:30px;color:var(--red);line-height:1.1}
.hero-sub{font-weight:700;font-size:10px;color:var(--ink);margin-top:4px}
.slider-arrows{position:absolute;right:40px;bottom:60px;display:flex;gap:2px}
.slider-arrows span{width:16px;height:18px;background:#3a3a3a;display:flex;align-items:center;justify-content:center}

.section{position:relative;display:flex;align-items:center;padding:0 40px}
.section-title{font-family:"Oswald",sans-serif;font-weight:500;font-size:13px;letter-spacing:.5px;color:var(--ink);margin-bottom:6px}
.section p,.section li{color:var(--muted);font-size:7.5px}
.section ul{list-style:none}

.use-cases{height:172px;margin-top:22px}
.chart-art{width:200px;height:110px;flex:none;border-radius:6px;background:linear-gradient(90deg,#f6b35a 0%,#e0585d 35%,#52bcc7 65%,#5a98cf 100%);opacity:.85}
.use-cases .body{margin-left:58px;flex:1}
.cols{display:flex;gap:40px}

.for-whom{height:176px}
.for-whom .body{width:320px}
.for-whom .body p{margin-bottom:6px}
.laptop-art{width:180px;height:130px;margin-left:auto;background:linear-gradient(180deg,#4bc0d0,#1f9fb0);border-radius:6px}

.vds{height:190px}
.gears-art{width:200px;height:150px;border-radius:50%;background:radial-gradient(circle,#5ec4d3 0%,#2aa5b8 55%,#fff 72%)}
.vds .body{margin-left:60px;flex:1}

.site-footer{position:absolute;left:0;top:960px;width:720px;height:212px;background:var(--foot);padding:28px 40px 0;display:flex;gap:44px}
.foot-col h4{font-size:8px;font-weight:700;color:var(--red);margin-bottom:8px;letter-spacing:.4px}
.foot-col li{list-style:none;color:var(--muted);font-size:7.5px;line-height:1.7}
.foot-col.contact{margin-left:auto}

.bottom-bar{position:absolute;left:0;top:1172px;width:720px;height:28px;background:var(--bar);padding:0 40px;display:flex;align-items:center;justify-content:space-between;color:#bbb;font-size:6px;line-height:1.4}
.legal a{color:#ddd;text-decoration:none;margin-right:4px}
.social{display:flex;gap:3px}
.social span{width:12px;height:12px;background:var(--blue)}
.social span:nth-child(3){background:var(--red)}
</style>
</head>
<body>
<div class="page">

  <header class="site-header">
    <div class="brand"><span class="brand-mark"></span>VandrelAI</div>
    <nav class="main-nav">
      <a class="active" href="#">HOME</a><a href="#">ABOUT US</a><a href="#">SERVICES</a><a href="#">PROJECT</a><a href="#">PRESS</a><a href="#">BLOG</a><a href="#">CONTACT</a>
    </nav>
  </header>

  <section class="hero">
    <div class="hero-art" role="img" aria-label="Illustration of a data cloud with round analytics icons floating above it"></div>
    <div class="hero-text">
      <h1 class="hero-title">Virtual Data Scientist</h1>
      <p class="hero-sub">Lorem Ipsum is simply dummy text of the printing</p>
    </div>
    <div class="slider-arrows">
      <span><svg width="6" height="8" viewBox="0 0 6 8"><path d="M5 0L1 4l4 4" stroke="#fff" fill="none" stroke-width="1.5"/></svg></span>
      <span><svg width="6" height="8" viewBox="0 0 6 8"><path d="M1 0l4 4-4 4" stroke="#fff" fill="none" stroke-width="1.5"/></svg></span>
    </div>
  </section>

  <section class="section use-cases">
    <div class="chart-art" role="img" aria-label="Illustration of a growth chart with a rising trend arrow"></div>
    <div class="body">
      <h2 class="section-title">USE CASES</h2>
      <div class="cols">
        <ul>
          <li>Big Data analytics that include:</li>
          <li>• Business Analytics</li>
          <li>• Fraud or Anomaly detection</li>
          <li>• Gaming Analytics and Prediction</li>
          <li>• Monitoring and analysis of IoT devices</li>
          <li>• Scientific Research and Discovery</li>
          <li>• Social Media Analytics</li>
        </ul>
        <ul>
          <li>Data Analysis and Discovery [Security]</li>
          <li>• predicting attacks and unknown insights</li>
          <li>• Predictions [Security Risk]</li>
          <li>• providing insight into the future</li>
          <li>• What-If Scenarios [Healthcare]</li>
          <li>• predicting related risk of possible outcomes</li>
          <li>• Recommendations [Security Info]</li>
        </ul>
      </div>
    </div>
  </section>

  <section class="section for-whom">
    <div class="body">
      <h2 class="section-title">FOR WHOM</h2>
      <p>Lorem Ipsum has been the industry's standard dummy text ever since the 1500s, when an unknown printer took a galley of type and scrambled it to make a type specimen book. It has survived not only five centuries.</p>
      <p>The VandrelAI Big data analytics engine can be adopted by any:<br>• CIOs<br>• for feature provisioning or enhancements<br>• Enterprise Users<br>• for enabling their software apps with customized<br>predictive and prescriptive analytic capabilities for their expected data</p>
    </div>
    <div class="laptop-art" role="img" aria-label="Illustration of a laptop showing analytics charts"></div>
  </section>

  <section class="section vds">
    <div class="gears-art" role="img" aria-label="Illustration of interlocking gears representing the analytics engine"></div>
    <div class="body">
      <h2 class="section-title">VIRTUAL DATA SCIENTIST</h2>
      <p>Lorem Ipsum has been the industry's standard dummy text ever since the 1500s, when an unknown printer took a galley of type and scrambled it to make a type specimen book. It has survived not only five centuries, but also the leap into electronic typesetting, remaining essentially unchanged. It was popularised in the 1960s with the release of sheets containing Lorem Ipsum passages, and more recently with desktop publishing software including versions of Lorem Ipsum.</p>
    </div>
  </section>

  <footer class="site-footer">
    <div class="foot-col"><h4>LINK</h4><ul><li>Services</li><li>Projects</li><li>Presentation</li></ul></div>
    <div class="foot-col"><h4>SPECIALISTS</h4><ul><li>Commercial</li><li>Residential</li><li>Luxury</li></ul></div>
    <div class="foot-col"><h4>ADVICE</h4><ul><li>FAQ</li><li>Support</li></ul></div>
    <div class="foot-col"><h4>AGENCIES</h4><ul><li>Sign Up</li><li>Forums</li><li>Promotions</li></ul></div>
    <div class="foot-col contact"><h4>CONTACT US</h4><ul><li>14 Larkfield Lane, Norbridge 2210</li><li>Phone: +1 555 014 2290</li><li>Email: hello@vandrel.example</li></ul></div>
  </footer>

  <div class="bottom-bar">
    <div class="legal">
      <div><a href="#">Privacy Policy</a>| <a href="#">Terms of Use</a>| <a href="#">About Us</a>| <a href="#">Sitemap</a></div>
      <div>Copyright © 2015. All Rights</div>
    </div>
    <div class="social"><span></span><span></span><span></span><span></span><span></span></div>
  </div>

</div>
</body>
</html>
```